Album art for soul / electronic band

Album art for a singer / producer duo. Art should be similar to the copper lantern album art and be consistent with the color scheme in the attached band photo. The name of the album is corvelha (portuguese for delicate). Please do not include the photo in your design. Design should center around water.

Target Market(s)

Gen X / Millenial soul music fans

Industry/Entity Type

music

Font styles to use
Sans Serif

Requirements
Must have
• Clean modern look, photo or artwork.
Nice to have
• It should look like album art from groups in the same genre such as the Copper Lantern, Brasskite, K. Dunmore, Orrin Vale
Should not have
• band photo, musical notes, any music iconography

```html
<!DOCTYPE html>
<html lang="en">
<head>
<meta charset="UTF-8">
<title>Lumen Vare — Corvelha</title>
<link rel="stylesheet" href="https://fonts.googleapis.com/css2?family=Montserrat:wght@200;800&display=swap">
<style>
  :root {
    --paper-light: #c4bfb2;
    --paper-mid: #aea99b;
    --haze: #8f8b80;
    --shadow-deep: #1f2a28;
    --shadow-soft: #3a403c;
    --focal-dark: #2b3230;
    --ripple-line: rgba(255, 255, 255, 0.55);
    --ripple-shade: rgba(31, 42, 40, 0.35);
    --type-white: #ffffff;
  }
  html, body {
    margin: 0;
    padding: 0;
    width: 1200px;
    height: 1200px;
    overflow: hidden;
    background: var(--shadow-deep);
  }
  .album-cover {
    position: relative;
    width: 1200px;
    height: 1200px;
    overflow: hidden;
  }
  .cover-artwork {
    position: absolute;
    inset: 0;
    background:
      radial-gradient(ellipse 70% 40% at 30% 38%, var(--paper-light) 0%, rgba(196,191,178,0) 70%),
      radial-gradient(ellipse 55% 55% at 100% 100%, var(--shadow-deep) 0%, rgba(31,42,40,0.9) 40%, rgba(31,42,40,0) 78%),
      radial-gradient(ellipse 120% 28% at 40% 108%, var(--shadow-deep) 0%, rgba(31,42,40,0.75) 45%, rgba(31,42,40,0) 82%),
      radial-gradient(ellipse 22% 45% at 104% 30%, var(--shadow-soft) 0%, rgba(58,64,60,0) 75%),
      radial-gradient(ellipse 25% 12% at 92% 2%, var(--shadow-soft) 0%, rgba(58,64,60,0) 80%),
      linear-gradient(180deg, var(--paper-mid) 0%, var(--paper-light) 40%, var(--haze) 72%, var(--shadow-soft) 100%);
  }
  .focal-subject {
    position: absolute;
    inset: 0;
    width: 1200px;
    height: 1200px;
  }
  .water-ripples {
    position: absolute;
    inset: 0;
    width: 1200px;
    height: 1200px;
  }
  .ripple-ring {
    fill: none;
    stroke: var(--ripple-line);
    stroke-width: 1.4;
  }
  .ripple-ring--faint { stroke-opacity: 0.5; }
  .ripple-ring--fainter { stroke-opacity: 0.25; }
  .ripple-shade {
    fill: none;
    stroke: var(--ripple-shade);
    stroke-width: 1.2;
  }
  .cover-titles {
    position: absolute;
    top: 130px;
    right: 78px;
    text-align: right;
    color: var(--type-white);
    font-family: "Montserrat", sans-serif;
    text-transform: uppercase;
    line-height: 1;
  }
  .artist-name {
    margin: 0;
    font-weight: 800;
    font-size: 35px;
    letter-spacing: 40px;
    margin-right: -40px;
  }
  .album-title {
    margin: 22px 0 0;
    font-weight: 200;
    font-size: 37px;
    letter-spacing: 46px;
    margin-right: -46px;
  }
</style>
</head>
<body>
  <main class="album-cover">
    <div class="cover-artwork" role="img" aria-label="Soft-focus sepia photograph of a hazy pale background darkening toward the lower right"></div>

    <svg class="focal-subject" viewBox="0 0 1200 1200" role="img" aria-label="Butterfly resting on a thin budding stem, with a budding branch crossing the lower half, in soft focus">
      <defs>
        <filter id="soft-focus" x="-50%" y="-50%" width="200%" height="200%">
          <feGaussianBlur stdDeviation="10"/>
        </filter>
        <filter id="deep-focus" x="-50%" y="-50%" width="200%" height="200%">
          <feGaussianBlur stdDeviation="22"/>
        </filter>
      </defs>
      <ellipse cx="935" cy="465" rx="62" ry="70" fill="var(--focal-dark)" opacity="0.8" filter="url(#soft-focus)"/>
      <ellipse cx="540" cy="930" rx="420" ry="40" transform="rotate(-9 540 930)" fill="var(--focal-dark)" opacity="0.35" filter="url(#deep-focus)"/>
      <ellipse cx="880" cy="700" rx="30" ry="170" transform="rotate(-14 880 700)" fill="var(--focal-dark)" opacity="0.25" filter="url(#deep-focus)"/>
    </svg>

    <svg class="water-ripples" viewBox="0 0 1200 1200" aria-hidden="true">
      <ellipse class="ripple-ring" cx="460" cy="760" rx="70" ry="14"/>
      <ellipse class="ripple-shade" cx="460" cy="763" rx="72" ry="15"/>
      <ellipse class="ripple-ring ripple-ring--faint" cx="460" cy="760" rx="150" ry="30"/>
      <ellipse class="ripple-shade" cx="460" cy="764" rx="152" ry="31"/>
      <ellipse class="ripple-ring ripple-ring--fainter" cx="460" cy="760" rx="250" ry="50"/>
      <ellipse class="ripple-ring ripple-ring--fainter" cx="460" cy="760" rx="370" ry="74"/>
    </svg>

    <header class="cover-titles">
      <h1 class="artist-name">Lumen Vare</h1>
      <h2 class="album-title">Corvelha</h2>
    </header>
  </main>
</body>
</html>
```